I WAS JUST GIVING A SIZE THAT THE LABEL NEEDS TO BE ON OUR PACKAGING BAGS, IT IS 4X6. PLEASE MAKE SURE THAT DESIGN WILL FIT ON THAT SIZE.

We are looking to have you design the packaging for our coffee that will be sold online. The basics that we want on all the different varieties is our company name "Halvorsen's Gourmet Coffee & tagline " Gourmet Coffee for the Everyday Coffee Lover" and logo which is attached. If you ffind a different logo and want to change the colors in the logo, we are open to any suggestions. Our thoughts are travel the world with your coffee, that why we went with compass star. We are looking to use black bags for all as well. We would like a different picture background that is relatable to the type of coffee, if possible. The colors need to pop on the black bag. We need designs for the following flavors of coffee...

Brazilian Dark Roast
Columbian Supremo
100% Columbian Dark Roast
French Vanilla
Velvet Meadow
Kona Blend
Jamaican Blue Mountain Blend
Sumatra
Hazelnut
Irish Cream
Hawaiian Macadamia Nut Blend
Amaretto

All these flavors will be sold in 5# and 2# packages

```html
<!DOCTYPE html>
<html lang="en">
<head>
<meta charset="UTF-8">
<title>Halvorsen's Gourmet Coffee – Label Range</title>
<link rel="stylesheet" href="https://fonts.googleapis.com/css2?family=Asap+Condensed:wght@700&family=Questrial&display=swap">
<style>
  :root {
    --page-bg: #e8ebeb;
    --bean-dark: #4a2614;
    --bean-mid: #6e3a1c;
    --bean-light: #7f4522;
    --panel-cream: #eec97f;
    --plate-cream: #f6e7c4;
    --panel-ink: #2a1a10;
    --name-white: #ffffff;
    --brand-ink: #7a1a1d;
    --brazil-green: #0a9444;
    --brazil-yellow: #f6c31a;
    --brazil-blue: #2a55a8;
    --france-blue: #2f55a4;
    --france-white: #ffffff;
    --france-red: #ea1d25;
    --colombia-blue: #22449a;
    --colombia-yellow: #fdd20d;
    --colombia-red: #d21f29;
  }
  * { margin: 0; padding: 0; box-sizing: border-box; }
  html, body { width: 1200px; height: 877px; overflow: hidden; }
  body { background: var(--page-bg); font-family: "Questrial", sans-serif; }

  .range { position: relative; width: 1200px; height: 877px; }

  .label {
    position: absolute; top: 215px;
    width: 300px; height: 447px; overflow: hidden;
    box-shadow: 0 6px 18px rgba(0,0,0,0.18);
  }
  .label--brazil { left: 90px; }
  .label--france { left: 450px; }
  .label--colombia { left: 810px; }

  .label__beans {
    position: absolute; inset: 0;
    background: radial-gradient(ellipse at 50% 55%, var(--bean-light), var(--bean-mid) 55%, var(--bean-dark));
  }

  .label__banner {
    position: absolute; top: 0; left: 0; width: 300px; height: 196px;
  }
  .label--brazil .label__banner {
    background: linear-gradient(180deg, var(--brazil-green) 0%, #3aa04a 60%, var(--brazil-green) 100%);
  }
  .label--france .label__banner {
    background: linear-gradient(90deg, var(--france-blue) 0%, #b9c4de 50%, var(--france-red) 100%);
  }
  .label--colombia .label__banner {
    background: linear-gradient(90deg, var(--colombia-blue) 0%, #e8c73a 50%, var(--colombia-red) 100%);
  }

  .label__rule {
    position: absolute; top: 196px; left: 0; width: 300px; height: 7px;
  }
  .label--brazil .label__rule { background: var(--brazil-blue); }
  .label--france .label__rule { background: var(--france-white); }
  .label--colombia .label__rule { background: var(--colombia-yellow); }

  .label__plate {
    position: absolute; top: 38px; left: 0; width: 300px; height: 68px;
    background: var(--plate-cream);
  }
  .label__brand {
    position: absolute; top: 45px; left: 0; width: 300px;
    text-align: center; color: var(--brand-ink);
    font-family: "Questrial", sans-serif; font-size: 22px; line-height: 27px;
  }

  .label__variety {
    position: absolute; top: 294px; left: 0; width: 300px;
    text-align: center; color: var(--name-white);
    font-family: "Asap Condensed", sans-serif; font-weight: 700; font-size: 18px;
  }
  .label__flag {
    position: absolute; top: 324px; left: 137px; width: 26px; height: 18px;
  }

  .label__panel { position: absolute; left: 0; bottom: 0; width: 300px; height: 64px; }
  .label__tagline {
    position: absolute; left: 0; bottom: 12px; width: 300px;
    text-align: center; color: var(--panel-ink);
    font-size: 14px; line-height: 19px;
  }
</style>
</head>
<body>
<main class="range">

  <article class="label label--brazil">
    <div class="label__beans" role="img" aria-label="Roasted coffee beans background"></div>
    <div class="label__banner" role="img" aria-label="Banner in Brazilian flag colours"></div>
    <div class="label__rule"></div>
    <div class="label__plate"></div>
    <p class="label__brand">Halvorsen's<br>Gourmet Coffee</p>
    <h2 class="label__variety">Brazilian Dark Roast</h2>
    <svg class="label__flag" viewBox="0 0 26 18" aria-label="Brazilian flag" role="img">
      <rect width="26" height="18" fill="var(--brazil-green)"/>
      <polygon points="13,2 24,9 13,16 2,9" fill="var(--brazil-yellow)"/>
      <circle cx="13" cy="9" r="4" fill="var(--brazil-blue)"/>
    </svg>
    <svg class="label__panel" viewBox="0 0 300 64" preserveAspectRatio="none" aria-hidden="true">
      <path d="M0,18 Q150,-14 300,18 L300,64 L0,64 Z" fill="var(--panel-cream)"/>
    </svg>
    <p class="label__tagline">Gourmet Coffee for the<br>Everyday Coffee Lover</p>
  </article>

  <article class="label label--france">
    <div class="label__beans" role="img" aria-label="Roasted coffee beans background"></div>
    <div class="label__banner" role="img" aria-label="Banner in French flag colours"></div>
    <div class="label__rule"></div>
    <div class="label__plate"></div>
    <p class="label__brand">Halvorsen's<br>Gourmet Coffee</p>
    <h2 class="label__variety">French Vanilla</h2>
    <svg class="label__flag" viewBox="0 0 26 18" aria-label="French flag" role="img">
      <rect width="9" height="18" fill="var(--france-blue)"/>
      <rect x="9" width="8" height="18" fill="var(--france-white)"/>
      <rect x="17" width="9" height="18" fill="var(--france-red)"/>
    </svg>
    <svg class="label__panel" viewBox="0 0 300 64" preserveAspectRatio="none" aria-hidden="true">
      <path d="M0,18 Q150,-14 300,18 L300,64 L0,64 Z" fill="var(--panel-cream)"/>
    </svg>
    <p class="label__tagline">Gourmet Coffee for the<br>Everyday Coffee Lover</p>
  </article>

  <article class="label label--colombia">
    <div class="label__beans" role="img" aria-label="Roasted coffee beans background"></div>
    <div class="label__banner" role="img" aria-label="Banner in Colombian flag colours"></div>
    <div class="label__rule"></div>
    <div class="label__plate"></div>
    <p class="label__brand">Halvorsen's<br>Gourmet Coffee</p>
    <h2 class="label__variety">Columbian Supremo</h2>
    <svg class="label__flag" viewBox="0 0 26 18" aria-label="Colombian flag" role="img">
      <rect width="26" height="9" fill="var(--colombia-yellow)"/>
      <rect y="9" width="26" height="4.5" fill="var(--colombia-blue)"/>
      <rect y="13.5" width="26" height="4.5" fill="var(--colombia-red)"/>
    </svg>
    <svg class="label__panel" viewBox="0 0 300 64" preserveAspectRatio="none" aria-hidden="true">
      <path d="M0,18 Q150,-14 300,18 L300,64 L0,64 Z" fill="var(--panel-cream)"/>
    </svg>
    <p class="label__tagline">Gourmet Coffee for the<br>Everyday Coffee Lover</p>
  </article>

</main>
</body>
</html>
```